Business Card Design for Event Planning Company

Create a business card for event planning company using our new logo. After I pick the design, I will need files made for 6 employees. Our company provides event design & logistics services as well as venue management. The font should be sans serif and complementary to the logo. I will need to know the name of the font selected for the final design. The phone numbers listed should be separated by "." not "-"

Address for the card
PO Box 318, Washington, DC 20019

Card One
Lorna Pettibone
lpettibone@galavoyant.com
202.481.7730

Card Two
Miriam Okonkwo
mokonkwo@galavoyant.com
202.556.2047

Card Three
Tessa Varnholt
tvarnholt@galavoyant.com
978.620.4471

Card Four
Robin Fess
rfess@galavoyant.com
202.718.3362

Card Five
Ada-Rose Pelletan-Uzor
adarose@galavoyant.com
202.839.1205

Card Six
Beatrix Holloway
Beatrix@galavoyant.com
202.492.6618

Target Market(s)

Corporate/Non-Profit

Industry/Entity Type

Event Planning

Contact Information for Business Card

Address for the card

Card One
Lorna Pettibone
lpettibone@galavoyant.com
202.481.7730

Card Two
Miriam Okonkwo
202.556.2047

Card Three
Tessa Varnholt
978.620.4471

Card Four
Robin Fess
rfess@galavoyant.com
202.718.3362

Card Five
Ada-Rose Pelletan-Uzor
202.839.1205

Card Six
Beatrix Holloway
202.492.6618

Font styles to use
Sans Serif

Colors

Designer to choose colors to be used in the design.

Requirements
Must have
• Two-sided with logo
Should not have
• Extra colors or be too busy

```html
<!DOCTYPE html>
<html lang="en">
<head>
<meta charset="utf-8">
<title>Galavoyant business cards</title>
<link href="https://fonts.googleapis.com/css2?family=Questrial&display=swap" rel="stylesheet">
<style>
  :root {
    --backdrop: #3a3a3c;
    --card: #ffffff;
    --teal: #5fa6a2;
    --ink: #1c1a1d;
    --text: #2e2e2e;
  }
  * { margin: 0; padding: 0; box-sizing: border-box; }
  html, body { width: 1200px; height: 900px; overflow: hidden; }
  body {
    position: relative;
    background: var(--backdrop);
    font-family: "Questrial", "Century Gothic", sans-serif;
    color: var(--text);
  }
  .card {
    position: absolute;
    width: 513px;
    height: 296px;
    background: var(--card);
    border-radius: 22px;
    overflow: hidden;
  }
  .card--front { left: 73px; top: 138px; }
  .card--logo-side { left: 616px; top: 138px; }
  .card--contact { left: 344px; top: 465px; }

  /* front */
  .front-band { position: absolute; top: 0; bottom: 0; }
  .front-band--teal { left: 0; width: 220px; background: var(--teal); }
  .front-band--ink { left: 220px; width: 120px; background: var(--ink); }
  .front-name {
    position: absolute; right: 38px; top: 90px;
    font-size: 17px; color: var(--teal); letter-spacing: 0.2px;
  }

  /* logo side */
  .brand-lockup {
    position: absolute; left: 0; right: 0; top: 118px;
    display: flex; flex-direction: column; align-items: center; gap: 8px;
  }
  .brand-dot { width: 22px; height: 22px; border-radius: 50%; background: var(--teal); }
  .brand-name { font-size: 30px; color: var(--ink); letter-spacing: 0.3px; line-height: 1; }

  /* contact side */
  .contact-brand {
    position: absolute; left: 48px; top: 42px;
    display: flex; flex-direction: column; align-items: flex-start; gap: 8px;
  }
  .contact-brand .brand-dot { margin-left: 78px; }
  .person-name {
    position: absolute; right: 48px; top: 176px;
    font-size: 16px; color: var(--teal);
  }
  .postal {
    position: absolute; left: 48px; top: 216px;
    font-size: 14px; line-height: 22.5px; color: var(--text); font-style: normal;
  }
  .contact-list {
    position: absolute; right: 48px; top: 216px;
    list-style: none; font-size: 14px; line-height: 22.5px; text-align: right;
  }
  .contact-list li { display: flex; justify-content: flex-end; align-items: center; gap: 6px; }
  .contact-icon { width: 14px; height: 14px; flex: none; }
</style>
</head>
<body>

<section class="card card--front" aria-label="Card front">
  <div class="front-band front-band--teal"></div>
  <div class="front-band front-band--ink"></div>
  <p class="front-name">galavoyant</p>
</section>

<section class="card card--logo-side" aria-label="Card back, brand side">
  <div class="brand-lockup">
    <span class="brand-dot"></span>
    <p class="brand-name">galavoyant</p>
  </div>
</section>

<section class="card card--contact" aria-label="Card back, contact side">
  <div class="contact-brand">
    <span class="brand-dot"></span>
    <p class="brand-name">galavoyant</p>
  </div>

  <p class="person-name">Ada-Rose Pelletan-Uzor</p>

  <address class="postal">
    PO Box 318<br>
    Washington<br>
    DC 20019
  </address>

  <ul class="contact-list">
    <li>202.839.1205
      <svg class="contact-icon" viewBox="0 0 14 14" aria-hidden="true">
        <circle cx="7" cy="7" r="7" fill="var(--teal)"/>
        <rect x="4.6" y="3" width="4.8" height="8" rx="1" fill="none" stroke="#fff" stroke-width="1.1"/>
        <circle cx="7" cy="9.6" r="0.6" fill="#fff"/>
      </svg>
    </li>
    <li>adarose@galavoyant.com
      <svg class="contact-icon" viewBox="0 0 14 14" aria-hidden="true">
        <circle cx="7" cy="7" r="7" fill="var(--teal)"/>
        <rect x="3.4" y="4.4" width="7.2" height="5.2" rx="0.6" fill="#fff"/>
        <path d="M3.6 4.7 L7 7.4 L10.4 4.7" fill="none" stroke="var(--teal)" stroke-width="0.9"/>
      </svg>
    </li>
    <li>www.galavoyant.com
      <svg class="contact-icon" viewBox="0 0 14 14" aria-hidden="true">
        <circle cx="7" cy="7" r="7" fill="var(--teal)"/>
        <circle cx="7" cy="7" r="3.8" fill="none" stroke="#fff" stroke-width="0.9"/>
        <ellipse cx="7" cy="7" rx="1.7" ry="3.8" fill="none" stroke="#fff" stroke-width="0.8"/>
        <line x1="3.2" y1="7" x2="10.8" y2="7" stroke="#fff" stroke-width="0.8"/>
      </svg>
    </li>
  </ul>
</section>

</body>
</html>
```